Brightwell Giving Inc

We need a full re-design of our non-profit organization website (www.brightwellgiving.org). Ideally, we are looking to make it more attractive, user-friendly, and interactive with our business model.

Please make sure to user colors that ago with our logo.

We need a homepage done and we also need a content page done where we will use for the other pages to fill with content.

Target Market(s)

Clothes/textiles donations.

Industry/Entity Type

Charity

Number of Pages Required

2 page

Colors

Designer to choose colors to be used in the design.

Requirements
Must have
• It must match the styling of our logo and same colors as current website. (www.brightwellgiving.org)
Nice to have
• Sleek homepage that is easy to understand and get our main points across.

```html
<!DOCTYPE html>
<html lang="en">
<head>
<meta charset="utf-8">
<title>Brightwell Giving Inc</title>
<link href="https://fonts.googleapis.com/css2?family=Roboto+Slab:wght@300;400;700&family=Open+Sans:wght@400;600;700&display=swap" rel="stylesheet">
<style>
:root{
  --green:#5b9d2c;
  --green-dark:#3d7a1d;
  --green-light:#8cc63f;
  --green-pale:#b9dd8c;
  --red:#c8171e;
  --yellow:#f4c414;
  --ink:#333;
  --muted:#777;
  --wash:#eef3ea;
  --grey:#ececec;
  --footer:#2a2a2a;
  --footer-deep:#1d1d1d;
}
*{box-sizing:border-box;margin:0;padding:0}
html,body{width:1200px;height:4509px;overflow:hidden}
body{position:relative;font-family:"Open Sans",sans-serif;color:var(--ink);background:#fff;font-size:13px}
.abs{position:absolute}
h2,h3,h4{font-family:"Roboto Slab",serif;font-weight:400}
.btn-red{display:inline-block;background:var(--red);color:#fff;font-family:"Roboto Slab",serif;font-size:13px;padding:9px 18px;border:none}
.section-title{font-family:"Roboto Slab",serif;font-size:26px;text-align:center;color:#222}
.divider{display:flex;align-items:center;justify-content:center;gap:8px;margin-top:8px}
.divider span{width:40px;height:1px;background:#bbb}
.photo{background:linear-gradient(135deg,#8a9d6d,#4f6b35 60%,#c7b07a)}

/* header */
.site-header{top:0;left:0;width:1200px;height:76px;background:#fff;box-shadow:0 1px 4px rgba(0,0,0,.1);z-index:3}
.brand{left:52px;top:18px;display:flex;align-items:center;gap:10px}
.brand-mark{width:36px;height:36px;background:var(--green)}
.brand-name{font-family:"Roboto Slab",serif;font-weight:700;color:var(--green-dark);font-size:18px;line-height:1}
.brand-tag{font-size:9px;color:var(--muted);margin-top:3px}
.main-nav{right:40px;top:30px;display:flex;gap:22px;font-size:11px;text-transform:uppercase;color:#555}
.main-nav .active{color:var(--green)}

/* hero */
.hero{top:76px;left:0;width:1200px;height:780px;background:linear-gradient(120deg,#9ab36b 0%,#5f7f3a 35%,#3b5a26 65%,#6d8a43 100%)}
.hero-frame{left:720px;top:70px;width:330px;height:360px;border:2px solid rgba(255,255,255,.85);padding:50px 20px 0 30px}
.hero-frame p{font-family:"Roboto Slab",serif;color:#fff;font-size:26px;line-height:1.15}
.hero-frame strong{display:block;font-family:"Roboto Slab",serif;color:var(--yellow);font-size:40px;font-weight:700;line-height:1.1;margin-bottom:6px}
.hero-frame .btn-red{margin:30px 0 0 60px}
.heart{position:absolute}

.intro-boxes{top:640px;left:146px;width:915px;height:255px;display:flex;z-index:2}
.intro-box{flex:1;padding:22px 22px;color:#fff;position:relative}
.intro-box h3{font-size:17px;font-weight:700;margin-bottom:16px}
.intro-box p{font-size:10.5px;line-height:1.6;margin-bottom:18px}
.intro-box .btn{display:inline-block;border:1px solid #fff;padding:5px 14px;font-size:11px;color:#fff}
.box-about{background:var(--green-dark)}
.box-sponsors{background:var(--green-light)}
.box-find{background:var(--green-pale);color:#2a3d1a;border:3px solid #fff}
.box-find h3{color:#2a3d1a}
.box-find .btn{border-color:#2a3d1a;color:#2a3d1a}
.find-input{width:100%;height:26px;background:#fff;margin-bottom:10px}

/* why */
.why-photo{left:140px;top:955px;width:605px;height:330px;background:linear-gradient(160deg,#d9dde0,#b6bcc1 55%,#6d7b4f)}
.why{left:800px;top:960px;width:360px}
.why h2{font-size:22px;margin-bottom:10px}
.why h4{color:var(--green);font-size:14px;margin-bottom:18px}
.why ul{list-style:none}
.why li{font-size:12px;margin-bottom:9px;display:flex;align-items:center;gap:10px}
.why .btn-red{margin-top:10px}

/* how */
.how{top:1330px;left:0;width:1200px;height:640px;background:var(--wash)}
.how-text{left:140px;top:60px;width:460px}
.how-text h2{font-size:24px;padding-bottom:8px;border-bottom:2px solid var(--green);display:inline-block;margin-bottom:20px}
.how-intro{font-family:"Roboto Slab",serif;font-weight:700;font-size:12px;line-height:1.55;margin-bottom:24px}
.step{display:flex;gap:18px;margin-bottom:22px}
.step-icon{flex:none;width:42px;height:42px;background:var(--green);display:flex;align-items:center;justify-content:center}
.step h4{font-size:14px;margin-bottom:5px}
.step p{font-size:11px;color:#666;line-height:1.5}
.how-photo{left:640px;top:0;width:560px;height:640px;background:linear-gradient(135deg,#d7c795,#9a6b3a 45%,#4b5d7a)}

/* gallery */
.gallery{top:2080px;left:0;width:1200px}
.gallery-row{position:absolute;top:120px;left:140px;display:flex;gap:30px}
.gallery-item{width:285px;height:225px}
.g1{background:linear-gradient(135deg,#4aa83a,#2e6e24)}
.g2{background:linear-gradient(135deg,#c5c9b8,#7d7f70)}
.g3{background:linear-gradient(135deg,#62b84a,#8a9aa8)}
.arrow{position:absolute;top:205px;width:38px;height:38px;border:1px solid #999;display:flex;align-items:center;justify-content:center;background:#fff}

/* news */
.news{top:2480px;left:0;width:1200px}
.news-panel{position:absolute;top:110px;left:0;width:1200px;height:265px;display:flex;border-top:1px solid #ddd;border-bottom:1px solid #ddd}
.news-list{width:305px;list-style:none;border-right:1px solid #ddd}
.news-list li{padding:12px 20px;font-size:11px;border-bottom:1px solid #ddd;line-height:1.4}
.news-list li.active{background:var(--green);color:#fff}
.news-article{width:455px;padding:28px 22px}
.news-article h3{font-size:16px;line-height:1.35;margin-bottom:14px}
.news-meta{font-size:10px;color:var(--muted);margin-bottom:14px;display:flex;gap:14px}
.news-article p{font-size:11px;color:#666;line-height:1.5}
.news-image{flex:1;background:#f2f2f2;display:flex;align-items:center;justify-content:center}
.news-flyer{width:320px;height:220px;background:linear-gradient(135deg,#fff,#d8d8d8)}

/* map */
.bins{top:3025px;left:0;width:1200px;height:460px;background:linear-gradient(160deg,#dfe6d8,#c9d6bd 50%,#e6e2cf)}
.bins-tab{left:0;top:0;background:var(--green);color:#fff;font-family:"Roboto Slab",serif;font-size:17px;padding:10px 30px}

/* contact */
.contact{top:3540px;left:0;width:1200px;height:580px;background:var(--grey)}
.contact .section-title{margin-top:45px}
.contact-form{position:absolute;top:160px;left:262px;width:676px}
.form-row{display:flex;gap:40px;margin-bottom:26px}
.field{flex:1;border-bottom:1px solid #bbb;padding:6px 0;font-size:11px;color:#888}
.textarea{height:150px;border:1px solid #bbb;padding:8px;font-size:11px;color:#888;background:#fff;margin-bottom:36px}
.submit{display:block;margin:0 auto;background:var(--green-dark);color:#fff;font-family:"Roboto Slab",serif;font-size:13px;padding:11px 30px;width:110px;text-align:center}

/* footer */
.site-footer{top:4145px;left:0;width:1200px;height:330px;background:var(--footer);color:#ccc}
.footer-col{position:absolute;top:34px}
.footer-col h4{color:#fff;font-size:18px;margin-bottom:18px}
.footer-col p{font-size:10.5px;line-height:1.6}
.addr{display:flex;gap:40px;margin-bottom:14px}
.addr strong{color:#fff;font-weight:600;display:block}
.links{display:grid;grid-template-columns:100px 100px;gap:4px;font-size:11px;margin-bottom:26px}
.sub-row{display:flex;margin:12px 0 22px}
.sub-row .input{width:260px;height:28px;background:#fff}
.sub-row .go{background:var(--green);color:#fff;font-size:11px;padding:6px 12px}
.search-row{display:flex}
.search-row .input{width:310px;height:28px;background:#fff}
.search-row .go{width:32px;height:28px;background:var(--green)}
.badges{display:flex;gap:10px;margin-top:14px;align-items:center}
.badge-note{width:36px;height:36px;background:var(--yellow)}
.badge-seal{width:44px;height:44px;border-radius:50%;background:#d6a319}
.footer-bar{top:4475px;left:0;width:1200px;height:34px;background:var(--footer-deep);color:#999;font-size:10px;padding:10px 35px}
.social-box{position:absolute;right:35px;top:6px;width:22px;height:22px;border:1px solid #777}
</style>
</head>
<body>

<header class="site-header abs">
  <div class="brand abs">
    <span class="brand-mark"></span>
    <div><div class="brand-name">BRIGHTWELL GIVING</div><div class="brand-tag">Think globally while donating locally</div></div>
  </div>
  <nav class="main-nav abs">
    <span class="active">Home</span><span>Missions</span><span>How It Works</span><span>About Us</span><span>Sponsors</span><span>Terms</span><span>Donate</span><span>Wall of Needs</span>
  </nav>
</header>

<section class="hero abs photo" role="img" aria-label="Smiling young girl holding sunflowers in a garden"></section>
<div class="abs" style="top:76px;left:0;width:1200px;height:780px">
  <div class="hero-frame abs">
    <p>We Make A Living By</p>
    <strong>What We Get</strong>
    <p>But We Make A Life By</p>
    <strong>What We Give</strong>
    <span class="btn-red">Donate Now</span>
  </div>
  <svg class="heart" style="left:695px;top:52px" width="40" height="36" viewBox="0 0 24 22"><path d="M12 21 2.5 11.5A5.5 5.5 0 0 1 12 4a5.5 5.5 0 0 1 9.5 7.5Z" fill="#c8171e"/></svg>
  <svg class="heart" style="left:1028px;top:410px" width="40" height="36" viewBox="0 0 24 22"><path d="M12 21 2.5 11.5A5.5 5.5 0 0 1 12 4a5.5 5.5 0 0 1 9.5 7.5Z" fill="#c8171e"/></svg>
</div>

<div class="intro-boxes abs">
  <div class="intro-box box-about">
    <h3>About Us</h3>
    <p>We are a family based non-profit organization in the name of Brightwell Giving Inc. We started this foundation in effort to help the community and each of its efforts give back to the less fortunate by the means of donating unwanted used clothing.</p>
    <span class="btn">Read More</span>
  </div>
  <div class="intro-box box-sponsors">
    <h3>Sponsors</h3>
    <p>We will mention all business sponsors on our website for the public to recognize who they are and their humble contributions. Businesses take the commitment of all the locations the Brightwell Giving organization becomes bigger and stronger.</p>
    <span class="btn">Read More</span>
  </div>
  <div class="intro-box box-find">
    <h3>Find Local Donation Place</h3>
    <p>Thank you for your big heart and kind help!<br>Enter Zip code to find local donation place</p>
    <div class="find-input"></div>
    <span class="btn">Search</span>
  </div>
</div>

<div class="why-photo abs" role="img" aria-label="Two volunteers standing in front of a donation truck"></div>
<section class="why abs">
  <h2>Why Choose Us</h2>
  <h4>Think Globally while Donating Locally</h4>
  <ul>
    <li><svg width="12" height="11" viewBox="0 0 24 22"><path d="M12 21 2.5 11.5A5.5 5.5 0 0 1 12 4a5.5 5.5 0 0 1 9.5 7.5Z" fill="#c8171e"/></svg>We are an open book organization</li>
    <li><svg width="12" height="11" viewBox="0 0 24 22"><path d="M12 21 2.5 11.5A5.5 5.5 0 0 1 12 4a5.5 5.5 0 0 1 9.5 7.5Z" fill="#c8171e"/></svg>We are a true 501(c)(3) non-profit organization</li>
    <li><svg width="12" height="11" viewBox="0 0 24 22"><path d="M12 21 2.5 11.5A5.5 5.5 0 0 1 12 4a5.5 5.5 0 0 1 9.5 7.5Z" fill="#c8171e"/></svg>Our goal is to be with and within the community</li>
    <li><svg width="12" height="11" viewBox="0 0 24 22"><path d="M12 21 2.5 11.5A5.5 5.5 0 0 1 12 4a5.5 5.5 0 0 1 9.5 7.5Z" fill="#c8171e"/></svg>Support anti-gas violence</li>
    <li><svg width="12" height="11" viewBox="0 0 24 22"><path d="M12 21 2.5 11.5A5.5 5.5 0 0 1 12 4a5.5 5.5 0 0 1 9.5 7.5Z" fill="#c8171e"/></svg>Help disaster victims of Hurricane zones</li>
    <li><svg width="12" height="11" viewBox="0 0 24 22"><path d="M12 21 2.5 11.5A5.5 5.5 0 0 1 12 4a5.5 5.5 0 0 1 9.5 7.5Z" fill="#c8171e"/></svg>Help Northeast parent &amp; child causes</li>
  </ul>
  <span class="btn-red">Donate Now</span>
</section>

<section class="how abs">
  <div class="how-text abs">
    <h2>How It Works</h2>
    <p class="how-intro">Recycling your old clothing is a significant humanitarian act. Brightwell Giving works towards simplifying the collection process by providing practical solutions for waste reduction. Brightwell Giving is particularly qualified to ensure an effort for an outstanding clothing recovery initiative.</p>
    <div class="step">
      <div class="step-icon"><svg width="20" height="20" viewBox="0 0 20 20" fill="none" stroke="#fff" stroke-width="2"><path d="M4 6h12l-1 12H5Z M2 6h16 M8 3h4"/></svg></div>
      <div><h4>Drop off clothing at your closest donation bin</h4><p>We have different collection procedures. For residents we can place a donation bin, a social customer drop off, or we can send a truck for pick-ups of large amounts of items.</p></div>
    </div>
    <div class="step">
      <div class="step-icon"><svg width="20" height="20" viewBox="0 0 20 20" fill="none" stroke="#fff" stroke-width="2"><path d="M6 3v14 M3 6l3-3 3 3 M14 17V3 M11 14l3 3 3-3"/></svg></div>
      <div><h4>We pick it up and take it to our sorting facility</h4><p>After our drivers pick up the clothing from our designated donation locations, the items are taken to our sorting facility where they are separated into three categories.</p></div>
    </div>
    <div class="step">
      <div class="step-icon"><svg width="20" height="20" viewBox="0 0 20 20"><text x="10" y="16" text-anchor="middle" fill="#fff" font-size="17" font-weight="700" font-family="Open Sans, sans-serif">$</text></svg></div>
      <div><h4>Charities get clothing. We pay you for the clothes</h4><p>Once we are done distributing our donated clothing to their appropriate channels, the proceeds from the sales are distributed to our team. The first distribution is in the form of donations to local charities.</p></div>
    </div>
    <span class="btn-red">Donate Now</span>
  </div>
  <div class="how-photo abs" role="img" aria-label="Volunteers handing over a bag of donated clothes beside a truck"></div>
</section>

<section class="gallery abs">
  <h2 class="section-title">Our Gallery</h2>
  <div class="divider"><span></span><svg width="14" height="13" viewBox="0 0 24 22"><path d="M12 21 2.5 11.5A5.5 5.5 0 0 1 12 4a5.5 5.5 0 0 1 9.5 7.5Z" fill="#c8171e"/></svg><span></span></div>
  <div class="arrow" style="left:42px"><svg width="10" height="12" viewBox="0 0 10 12"><path d="M8 1 2 6l6 5" fill="none" stroke="#555" stroke-width="2"/></svg></div>
  <div class="gallery-row">
    <div class="gallery-item g1" role="img" aria-label="Green donation bin on a trailer"></div>
    <div class="gallery-item g2" role="img" aria-label="Volunteer holding a donation flyer"></div>
    <div class="gallery-item g3" role="img" aria-label="Green clothing donation bins in a parking lot"></div>
  </div>
  <div class="arrow" style="left:1120px"><svg width="10" height="12" viewBox="0 0 10 12"><path d="M2 1l6 5-6 5" fill="none" stroke="#555" stroke-width="2"/></svg></div>
</section>

<section class="news abs">
  <h2 class="section-title">Latest News</h2>
  <div class="divider"><span></span><svg width="14" height="13" viewBox="0 0 24 22"><path d="M12 21 2.5 11.5A5.5 5.5 0 0 1 12 4a5.5 5.5 0 0 1 9.5 7.5Z" fill="#c8171e"/></svg><span></span></div>
  <div class="news-panel">
    <ul class="news-list">
      <li class="active">Brightwell Giving created the flyer for inform the people in Manhattan</li>
      <li>We are starting the charity projects to collect funds on our campaign page</li>
      <li>Charity Project Love Thy Neighbor - Elena</li>
      <li>Charity Project LOVE THY NEIGHBOR donation boxes</li>
      <li>Brightwell Giving online shop</li>
      <li>Brightwell Giving Street Sales</li>
    </ul>
    <article class="news-article">
      <h3>Brightwell Giving created the flyer for inform the people in Manhattan to help others by giving donation.</h3>
      <div class="news-meta"><span>May 14, 2017</span><span>Admin</span><span>0</span></div>
      <p>Brightwell Giving created the flyer for inform the people in Manhattan to help others by giving donation.</p>
    </article>
    <div class="news-image"><div class="news-flyer" role="img" aria-label="Folded donation flyer with photos"></div></div>
  </div>
</section>

<section class="bins abs" role="img" aria-label="Map of the region marked with donation bin locations">
  <div class="bins-tab abs">Brightwell Giving Bins</div>
</section>

<section class="contact abs">
  <h2 class="section-title">Easy To Be In Touch</h2>
  <div class="divider"><span></span><svg width="14" height="13" viewBox="0 0 24 22"><path d="M12 21 2.5 11.5A5.5 5.5 0 0 1 12 4a5.5 5.5 0 0 1 9.5 7.5Z" fill="#c8171e"/></svg><span></span></div>
  <div class="contact-form">
    <div class="form-row"><div class="field">Name</div><div class="field">Email</div></div>
    <div class="form-row"><div class="field">Website</div></div>
    <div class="textarea">Message</div>
    <span class="submit">Submit</span>
  </div>
</section>

<footer class="site-footer abs">
  <div class="footer-col" style="left:35px;width:440px">
    <h4>Contact Us</h4>
    <div class="addr">
      <p><strong>New York Office</strong>24 Orchard Lane, Millbrook<br>NY 12040<br>(555) 014-2290</p>
      <p><strong>New York Warehouse</strong>410 Riverbend Rd, Stonefield<br>NY 12077</p>
    </div>
    <div class="addr">
      <p><strong>Thrift Store</strong>88 Linden Street,<br>Fairhaven NY 12590</p>
      <div class="badges"><span class="badge-note"></span><span class="badge-note"></span><span class="badge-note"></span><span class="badge-seal"></span></div>
    </div>
  </div>
  <div class="footer-col" style="left:545px;width:230px">
    <h4>Quick Links</h4>
    <div class="links"><span>About Us</span><span>Donate</span><span>Missions</span><span>Wall Of Needs</span><span>How It Works</span><span>Disclaimers</span><span>Sponsors</span><span>Contact Us</span><span>News</span></div>
    <span class="btn-red">Donate Now</span>
  </div>
  <div class="footer-col" style="left:805px;width:360px">
    <h4>Newsletter</h4>
    <p>Subscribe to our newsletter for latest updates</p>
    <div class="sub-row"><div class="input"></div><span class="go">Subscribe</span></div>
    <h4>Find Local Donation Place</h4>
    <div class="search-row"><div class="input"></div><div class="go"></div></div>
  </div>
</footer>
<div class="footer-bar abs">© Copyright Brightwell Giving Inc. All rights reserved.<span class="social-box"></span></div>

</body>
</html>
```